Website for Company to help with House Restoration from Hurricane Damage

Crisp, Clean and Professional!

I need a FRONT page for a website. I need it created in photoshop with the layers intact. We DO NOT need the HTML or DRB for the site. Simply the design. Any fonts you use will need to be included if they are not standard. Please make sure any fonts you use in the body of the text are available for use on Google Fonts.

I have attached a word doc that lists the menu items and additional instructions.

A little about the company - after Hurricane Marlow - DRB developed a system which allows the house to be raised, the Tremlets installed, and the house reset on the Tremlets without the expense of moving the house or driving new pilings. This option can be installed in a matter of days with limited space and at a lower construction cost.

Please refer to the attached musthaves.doc and images that are included.

The main page must incorporate the menu, the attached photos w/ text underneath (text is in the word doc attached), and the text included in the word doc.

Standard footer with contact info as well.

If you have questions please contact us!
Updates

Designs are due by Friday! We will pick one this weekend.  We are unable to change it from 10 days to 5.  Thank you!!!

Target Market(s)

People who lost their homes or businesses due to a hurricane.

Industry/Entity Type

Construction

Requirements
Must have
• See attached musthaves.doc

```html
<!DOCTYPE html>
<html lang="en">
<head>
<meta charset="utf-8">
<title>DRB – Rebuild Safer, Stronger, Better</title>
<link rel="stylesheet" href="https://fonts.googleapis.com/css2?family=Open+Sans:wght@400;600;700&display=swap">
<style>
:root{
  --green:#7a8e55;
  --green-dark:#5f7042;
  --green-light:#a9ba86;
  --nav-divider:#b6c39c;
  --page-bg:#f3f3f1;
  --text:#4a4a4a;
  --frame:#dcdcd8;
  --white:#ffffff;
}
*{margin:0;padding:0;box-sizing:border-box}
html,body{width:1200px;height:886px;overflow:hidden}
body{
  font-family:"Open Sans",Arial,sans-serif;
  background:var(--page-bg);
  color:var(--text);
  position:relative;
}
.top-rule{position:absolute;left:0;top:0;width:1200px;height:5px;background:var(--green)}
.wrap{position:absolute;left:189px;width:823px}

/* header */
.brand{position:absolute;left:189px;top:38px;display:flex;align-items:center;gap:8px;
  font-size:34px;font-weight:700;color:var(--green-dark);letter-spacing:1px}
.brand-dot{width:16px;height:16px;border-radius:50%;background:var(--green-light)}
.contact-line{position:absolute;top:28px;right:189px;display:flex;align-items:center;
  font-size:12px;color:var(--text)}
.contact-line span{display:flex;align-items:center;gap:7px}
.contact-line .mail{margin-left:26px}

.main-nav{position:absolute;left:338px;top:65px;width:673px;height:45px;background:var(--green);
  border-radius:4px;display:flex;align-items:center;overflow:hidden}
.main-nav a{color:var(--white);text-decoration:none;font-size:12.2px;display:flex;align-items:center;
  height:100%;padding:0 12px;position:relative}
.main-nav a + a::before{content:"";position:absolute;left:0;top:17px;height:14px;width:1px;background:var(--nav-divider)}
.main-nav a.active{background:var(--green-light);padding:0 14px}
.main-nav a.active + a::before{display:none}

/* slider */
.slider{top:129px;height:343px;background:var(--white);border:1px solid var(--frame);padding:5px}
.slide{position:relative;width:100%;height:100%;
  background:linear-gradient(180deg,#8f7f95 0%,#d6a2a3 28%,#f1c7a6 42%,#6f6672 52%,#4d4554 70%,#837a80 85%,#9a9291 100%)}
.slide-caption{position:absolute;left:58px;top:132px}
.slide-caption p{display:inline-block;background:var(--green);color:var(--white);font-size:15.5px;
  font-weight:600;padding:2px 8px;line-height:21px;margin-bottom:5px}
.slide-arrow{position:absolute;top:132px}
.slide-arrow.prev{left:10px}
.slide-arrow.next{right:10px}

/* intro */
.intro-photo{position:absolute;left:189px;top:489px;width:256px;height:245px;background:var(--white);
  border:1px solid var(--frame);padding:5px}
.intro-photo div{width:100%;height:100%;background:radial-gradient(circle at 50% 50%,#c7b2a2 0%,#dccbbd 40%,#eceae6 80%)}
.intro-text{position:absolute;left:460px;top:487px;width:552px;font-size:11.2px;line-height:15.4px;
  text-align:justify}
.intro-text p + p{margin-top:10px}
.read-more{position:absolute;left:907px;top:705px;width:103px;height:29px;background:var(--green);
  color:var(--white);font-size:11.2px;border-radius:4px;display:flex;align-items:center;justify-content:center;
  text-decoration:none}

/* footer */
.site-footer{position:absolute;left:0;top:763px;width:1200px;height:75px;background:var(--green);
  color:var(--white);text-align:center;font-size:12.5px;line-height:17px;padding-top:16px}
.footer-bar{position:absolute;left:0;top:838px;width:1200px;height:48px;background:var(--green-dark);
  color:#d3dbc2;font-size:12.5px}
.copyright{position:absolute;left:189px;top:15px}
.footer-nav{position:absolute;right:189px;top:15px;display:flex}
.footer-nav a{color:#d3dbc2;text-decoration:none}
.footer-nav .sep{margin:0 12px}
</style>
</head>
<body>
<div class="top-rule"></div>

<header>
  <div class="brand"><span class="brand-dot"></span>DRB</div>
  <div class="contact-line">
    <span>
      <svg width="15" height="21" viewBox="0 0 15 21"><rect x="1" y="1" width="13" height="19" rx="2" fill="#7a8e55"/><rect x="3" y="3" width="9" height="5" fill="#f3f3f1"/><g fill="#f3f3f1"><rect x="3" y="10" width="2" height="2"/><rect x="6.5" y="10" width="2" height="2"/><rect x="10" y="10" width="2" height="2"/><rect x="3" y="14" width="2" height="2"/><rect x="6.5" y="14" width="2" height="2"/><rect x="10" y="14" width="2" height="2"/></g></svg>
      18004-0270
    </span>
    <span class="mail">
      <svg width="24" height="15" viewBox="0 0 24 15"><rect x="0" y="0" width="24" height="15" rx="1" fill="#7a8e55"/><path d="M1 1 L12 9 L23 1" stroke="#f3f3f1" stroke-width="1.5" fill="none"/></svg>
      SALES@DURABLERAISE.COM
    </span>
  </div>
  <nav class="main-nav">
    <a class="active" href="#">HOME</a>
    <a href="#">SERVICES</a>
    <a href="#">ABOUT US</a>
    <a href="#">PRODUCT SPECIFICATIONS</a>
    <a href="#">DESIGN DOCUMENTATION</a>
    <a href="#">CONTACT US</a>
  </nav>
</header>

<section class="wrap slider">
  <div class="slide" role="img" aria-label="Photo of a father and young child holding hands on a beach at sunset">
    <div class="slide-caption">
      <p>REBUILD SAFER, STRONGER, BETTER TO</p><br>
      <p>BUILD NEW LASTING MEMORIES</p>
    </div>
    <svg class="slide-arrow prev" width="30" height="70" viewBox="0 0 30 70"><path d="M28 1 L2 35 L28 69" stroke="#fff" stroke-width="1.5" fill="none"/></svg>
    <svg class="slide-arrow next" width="30" height="70" viewBox="0 0 30 70"><path d="M2 1 L28 35 L2 69" stroke="#fff" stroke-width="1.5" fill="none"/></svg>
  </div>
</section>

<section class="intro">
  <div class="intro-photo"><div role="img" aria-label="Photo of two hands holding a small model house"></div></div>
  <div class="intro-text">
    <p>Systems for extending the height of existing piles are not available on today’s market.&nbsp; Durable Raise Builders, LLC (DRB) has developed two systems to allow for Piles to be extended that provide superior structural support without corrosion and maintenance concerns.&nbsp; We provided two systems, a complete system, Pile Cap Extension Tremlets, and Pile Splice.&nbsp; These two systems allow a home to be raised to by up to 54”, higher extensions possible with additional design consideration for lateral support. Shown below is the full Piling Extension system, which connects to the top of the existing pile. The system modular and can be cut to meet specific needs of the home.</p>
    <p>Our Patented Piling system has been designed to withstand the corrosive environment of beach communities. The salt water and windblown sand corrodes unprotected materials, and yes, even stainless steel. Our system utilizes a high strength carbon fiber material that is corrosion proof from salt water and UV proof. The system will not erode, decay or loose strength over time. The system has three installation conditions, for raising a house on existing pilings, repairing damaged pilings, and for connecting new pilings to floor joists in new construction. The three options are generally described here</p>
  </div>
  <a class="read-more" href="#">READ MORE</a>
</section>

<footer>
  <div class="site-footer">
    Durable Raise Builders, LLC - PO Box 40512,&nbsp; Harbor Valley, PA 18004-0270 -(555) 014-2290<br>
    Email: sales@durableraise.com
  </div>
  <div class="footer-bar">
    <div class="copyright">Copyright © 2013 DRB</div>
    <nav class="footer-nav">
      <a href="#">Home</a><span class="sep">|</span>
      <a href="#">Service</a><span class="sep">|</span>
      <a href="#">About Us</a><span class="sep">|</span>
      <a href="#">Product Specifications</a><span class="sep">|</span>
      <a href="#">Design Documentation</a><span class="sep">|</span>
      <a href="#">Contact Us</a>
    </nav>
  </div>
</footer>
</body>
</html>
```